BRIM Outreach Partners Business Card Rebrand

Hello Designers! We are looking for help designing our new business card to go in conjunction with our company rebrand. Unfortunately, we have an event mid June that requires we get these printed ASAP (before our new website is launched.) We have a mostly complete Brand Book which I have uploaded to this request for your reference to company information, style, fonts. I've also enclosed our logo file in .eps & .jpg. Attached is a sample business card my boss liked but said was "too simple." I made it in Canva and do not profess to be a designer. NOT FOR DESIGN REFERENCE, ONLY FOR CONTEXT Here is what our old website looks like: https://brimoutreachpartners.com/.

```html
<!DOCTYPE html>
<html lang="en">
<head>
<meta charset="utf-8">
<title>BRIM Outreach Partners – Business Card</title>
<link href="https://fonts.googleapis.com/css2?family=Poppins:wght@400;500;700;800&display=swap" rel="stylesheet">
<style>
  :root {
    --stage: #c4c5c7;
    --card-white: #ffffff;
    --brand-blue: #4bb3e6;
    --pale-blue: #d9eefa;
    --ink: #151515;
    --text: #333333;
  }
  * { box-sizing: border-box; margin: 0; padding: 0; }
  html, body { width: 1200px; height: 876px; overflow: hidden; }
  body {
    background: var(--stage);
    font-family: "Poppins", sans-serif;
    display: flex;
    align-items: center;
    justify-content: center;
    gap: 60px;
  }
  .card {
    position: relative;
    width: 520px;
    height: 297px;
    overflow: hidden;
    box-shadow: 0 10px 24px rgba(0,0,0,0.18);
  }
  /* Front */
  .card-front { background: var(--card-white); }
  .front-decor {
    position: absolute;
    right: -70px;
    bottom: -150px;
    width: 360px;
    height: 360px;
    border-radius: 50%;
    background: var(--pale-blue);
  }
  .front-content { position: relative; padding: 26px 30px; }
  .wordmark {
    display: flex;
    align-items: center;
    gap: 10px;
    margin-bottom: 18px;
  }
  .wordmark-dot {
    width: 34px; height: 34px;
    border-radius: 50%;
    background: var(--brand-blue);
    flex: none;
  }
  .wordmark-name {
    font-weight: 800;
    font-size: 21px;
    color: var(--ink);
    letter-spacing: -0.3px;
    line-height: 1;
    white-space: nowrap;
  }
  .person-name {
    font-weight: 700;
    font-size: 21px;
    color: var(--ink);
    line-height: 1.1;
  }
  .person-title {
    font-size: 12px;
    color: var(--brand-blue);
    margin-bottom: 12px;
  }
  .contact-list { list-style: none; }
  .contact-item {
    display: flex;
    align-items: center;
    gap: 8px;
    font-size: 12.5px;
    color: var(--text);
    line-height: 1.75;
  }
  .contact-icon { width: 13px; height: 13px; flex: none; }
  .location {
    margin-top: 8px;
    font-size: 12.5px;
    font-weight: 500;
    color: var(--brand-blue);
  }
  /* Back */
  .card-back {
    background: var(--brand-blue);
    display: flex;
    align-items: center;
    justify-content: center;
  }
  .card-back .wordmark { margin: 0; gap: 14px; }
  .card-back .wordmark-dot { width: 54px; height: 54px; background: var(--card-white); }
  .card-back .wordmark-name { font-size: 29px; }
</style>
</head>
<body>
  <section class="card card-front" aria-label="Business card front">
    <div class="front-decor" aria-hidden="true"></div>
    <div class="front-content">
      <div class="wordmark">
        <span class="wordmark-dot" aria-hidden="true"></span>
        <span class="wordmark-name">BRIM Outreach Partners</span>
      </div>
      <h1 class="person-name">Daniel Marsh-Okafor</h1>
      <p class="person-title">Managing Partner</p>
      <ul class="contact-list">
        <li class="contact-item">
          <svg class="contact-icon" viewBox="0 0 16 16" aria-hidden="true"><path fill="#4bb3e6" d="M3.6 1.5l2.3 2.6-1.2 1.8a9 9 0 0 0 5.4 5.4l1.8-1.2 2.6 2.3-1.4 2.1C7 14.3 1.7 9 1.5 2.9z"/></svg>
          +1-303-555-0174
        </li>
        <li class="contact-item">
          <svg class="contact-icon" viewBox="0 0 16 16" aria-hidden="true"><rect x="1" y="3" width="14" height="10" rx="1" fill="#4bb3e6"/><path d="M1.5 3.8L8 9l6.5-5.2" stroke="#fff" stroke-width="1.3" fill="none"/></svg>
          daniel@brimoutreachpartners.com
        </li>
        <li class="contact-item">
          <svg class="contact-icon" viewBox="0 0 16 16" aria-hidden="true"><circle cx="8" cy="8" r="7" fill="#4bb3e6"/><path d="M1 8h14M8 1c-3 3.5-3 10.5 0 14M8 1c3 3.5 3 10.5 0 14" stroke="#fff" stroke-width="1" fill="none"/></svg>
          brimoutreachpartners.com
        </li>
      </ul>
      <p class="location">Denver, CO based (Mountain Time)</p>
    </div>
  </section>

  <section class="card card-back" aria-label="Business card back">
    <div class="wordmark">
      <span class="wordmark-dot" aria-hidden="true"></span>
      <span class="wordmark-name">BRIM Outreach Partners</span>
    </div>
  </section>
</body>
</html>
```